zumoKet - website to pay membership association fee

The main purpose of this site it to allow a pre-registered user to be able to view the membership fees for their membership association and pay the same in one of the ways offered by the portal.
You are required to create a graphical project only for the logon functions as a user, while omitting the back end/administration ones that will be decided later
The site, besides being responsive must be very intuitive in its function. The graphics must be bright.

Number of Pages Required

4 page

Requirements
Must have
• i need to see template for
• 1. Home page
• 2. Page after login. People can se one or more bill to Pay and decide to see more details or to pay.
• 3. Page to Pay. Choose the desired payment method five alternative

```html
<!DOCTYPE html>
<html lang="en">
<head>
<meta charset="utf-8">
<title>zumoKet – My Bills</title>
<link href="https://fonts.googleapis.com/css2?family=Roboto:wght@300;400;500&family=Roboto+Condensed:wght@400&display=swap" rel="stylesheet">
<style>
  :root {
    --blue: #0181d7;
    --panel: #eceff3;
    --line: #d6dde6;
    --field-line: #cfd6df;
    --text: #56617a;
    --text-soft: #8b94a6;
    --text-strong: #3f4a5e;
    --icon: #6b7587;
    --white: #ffffff;
  }
  * { box-sizing: border-box; margin: 0; padding: 0; }
  html, body { width: 1200px; height: 640px; overflow: hidden; background: var(--white); }
  body { position: relative; font-family: "Roboto", Arial, sans-serif; color: var(--text); }

  .side-menu { position: absolute; left: 21px; top: 117px; width: 216px; }
  .menu-head {
    height: 56px; background: var(--panel); display: flex; align-items: center;
    padding-left: 16px; gap: 9px; border-radius: 2px 2px 0 0;
    font-family: "Roboto Condensed", "Arial Narrow", sans-serif; font-size: 16px; color: var(--text-strong);
  }
  .menu-item {
    height: 40px; border-bottom: 1px solid var(--line); display: flex; align-items: center;
    padding-left: 24px; font-size: 12px; font-weight: 300; color: var(--text);
  }
  .menu-item.is-active { background: var(--blue); color: var(--white); font-weight: 400; border-bottom-color: var(--blue); }

  .filter-bar { position: absolute; left: 276px; top: 132px; display: flex; gap: 8px; }
  .filter-select {
    width: 192px; height: 36px; background: var(--panel); border: 1px solid var(--field-line); border-radius: 3px;
    display: flex; align-items: center; justify-content: space-between; padding: 0 12px;
    font-size: 12px; font-weight: 300; color: var(--text-soft);
  }
  .btn {
    background: var(--blue); color: var(--white); border: none; border-radius: 3px;
    font-family: inherit; font-size: 12px; font-weight: 500; letter-spacing: 0.1px;
    display: flex; align-items: center; justify-content: center;
  }
  .btn-apply { position: absolute; left: 877px; top: 134px; width: 253px; height: 35px; }
  .btn-pay { position: absolute; left: 747px; top: 477px; width: 253px; height: 35px; }

  .bills-table {
    position: absolute; left: 318px; top: 180px; width: 682px; table-layout: fixed;
    border-collapse: separate; border-spacing: 0; border: 1px solid var(--line); border-radius: 3px; font-size: 12px;
  }
  .bills-table th, .bills-table td {
    height: 40px; border-right: 1px solid var(--line); border-bottom: 1px solid var(--line); text-align: center;
  }
  .bills-table th:last-child, .bills-table td:last-child { border-right: none; }
  .bills-table tr:last-child td { border-bottom: none; }
  .bills-table th { background: var(--panel); font-weight: 400; color: var(--text); vertical-align: middle; }
  .bills-table th.col-ref-no { vertical-align: top; padding-top: 11px; }
  .bills-table .col-name { text-align: left; padding-left: 9px; }
  .bills-table td.col-name { font-weight: 300; color: var(--text-soft); }
  .bills-table td.col-amount { color: var(--text); }
  .check {
    display: inline-flex; width: 20px; height: 20px; border: 1px solid var(--field-line);
    background: var(--panel); border-radius: 3px; align-items: center; justify-content: center; vertical-align: middle;
  }
</style>
</head>
<body>
  <nav class="side-menu">
    <div class="menu-head">
      <svg width="26" height="16" viewBox="0 0 26 16" aria-hidden="true">
        <path d="M0.5 8 L2.5 6.8 L2.5 9.2Z" fill="#8b94a6"/>
        <rect x="6" y="1" width="19" height="2" rx="1" fill="#8b94a6"/>
        <rect x="6" y="7" width="19" height="2" rx="1" fill="#8b94a6"/>
        <rect x="6" y="13" width="19" height="2" rx="1" fill="#8b94a6"/>
      </svg>
      MENU
    </div>
    <div class="menu-item is-active">My Bills</div>
    <div class="menu-item">Pay Bills</div>
    <div class="menu-item">Logout</div>
    <div class="menu-item"></div>
    <div class="menu-item"></div>
    <div class="menu-item"></div>
  </nav>

  <div class="filter-bar">
    <div class="filter-select">Fiscal Code
      <svg width="12" height="8" viewBox="0 0 12 8"><path d="M1 1.5 L6 6 L11 1.5" fill="none" stroke="#7d8798" stroke-width="1.4"/></svg></div>
    <div class="filter-select">Association Name
      <svg width="12" height="8" viewBox="0 0 12 8"><path d="M1 1.5 L6 6 L11 1.5" fill="none" stroke="#7d8798" stroke-width="1.4"/></svg></div>
    <div class="filter-select">Reference Category
      <svg width="12" height="8" viewBox="0 0 12 8"><path d="M1 1.5 L6 6 L11 1.5" fill="none" stroke="#7d8798" stroke-width="1.4"/></svg></div>
  </div>
  <button class="btn btn-apply">APPLY FILTER</button>

  <table class="bills-table">
    <colgroup>
      <col style="width:46px"><col style="width:138px"><col style="width:94px"><col style="width:137px">
      <col style="width:96px"><col style="width:77px"><col style="width:94px">
    </colgroup>
    <thead>
      <tr>
        <th><svg width="14" height="14" viewBox="0 0 14 14" aria-label="Select"><path d="M7 1.5H1.5v11h11V7" fill="none" stroke="#6b7587" stroke-width="1.4"/><path d="M5 9l0.6-2.4L11 1.2 12.8 3 7.4 8.4Z" fill="#6b7587"/></svg></th>
        <th class="col-name">Association Name</th>
        <th>Fiscal Code</th>
        <th>Reference Category</th>
        <th>Bill Date</th>
        <th class="col-ref-no">Bill Ref No</th>
        <th>Bill Amount</th>
      </tr>
    </thead>
    <tbody>
      <tr><td><span class="check"></span></td><td class="col-name">My Association 1</td><td></td><td></td><td></td><td></td><td class="col-amount">$145</td></tr>
      <tr><td><span class="check"><svg width="12" height="10" viewBox="0 0 12 10"><path d="M1 5l3.5 3.5L11 1.5" fill="none" stroke="#6b7587" stroke-width="1.4"/></svg></span></td><td class="col-name">My Association 1</td><td></td><td></td><td></td><td></td><td class="col-amount">$29</td></tr>
      <tr><td><span class="check"><svg width="12" height="10" viewBox="0 0 12 10"><path d="M1 5l3.5 3.5L11 1.5" fill="none" stroke="#6b7587" stroke-width="1.4"/></svg></span></td><td class="col-name">My Association 2</td><td></td><td></td><td></td><td></td><td class="col-amount">$59</td></tr>
      <tr><td><span class="check"></span></td><td class="col-name">My Association 2</td><td></td><td></td><td></td><td></td><td class="col-amount">$129</td></tr>
      <tr><td><span class="check"><svg width="12" height="10" viewBox="0 0 12 10"><path d="M1 5l3.5 3.5L11 1.5" fill="none" stroke="#6b7587" stroke-width="1.4"/></svg></span></td><td class="col-name">My Association 2</td><td></td><td></td><td></td><td></td><td class="col-amount">$185</td></tr>
      <tr><td><span class="check"></span></td><td class="col-name">My Association 3</td><td></td><td></td><td></td><td></td><td class="col-amount">$215</td></tr>
    </tbody>
  </table>

  <button class="btn btn-pay">PAY BILLS</button>
</body>
</html>
```